we are a mobile auto windscreen replacement business we are looking for a smart, stylish designed card on a matte black base color with large metallic silver KLT (similar to the vexapad box)
over the whole face of the card but down the bottom have (your local automotive & machinery glass specialist) & over the back

Reason: I'm looking for a design like no other something that really wows people to grab a card & use my business

Target Market(s)

Adults in western countries that own an automotive fleet company or anybody that owns a car

Industry/Entity Type

Automotive

Contact Information for Business Card

front: KLTautoglaze
Back: MORRIS 0438 62 57 84 Abn: 52807341196
morris@kltautoglaze.com.au & www.kltautoglaze.com.au

Logo styles of interest
Lettermark Logo
Requirements
Must have
• Metallic font on matte background
Nice to have
• 3D font that's glass or the word KLT smashed into glass on a black background I've added some pictures that maybe you could incorporate in the background or font it would be great to see a professionals ideas

```html
<!DOCTYPE html>
<html lang="en">
<head>
<meta charset="utf-8">
<title>KLT autoglaze – business card</title>
<link href="https://fonts.googleapis.com/css2?family=Lato:wght@400;700;900&display=swap" rel="stylesheet">
<style>
  :root {
    --page: #e9e6e1;
    --card-black: #050505;
    --silver: #c9ccd1;
    --white: #ffffff;
    --muted: #8d8d8d;
    --glass-light: #d8d8d8;
    --glass-mid: #5a5a5a;
  }
  * { box-sizing: border-box; margin: 0; padding: 0; }
  html, body { width: 1200px; height: 1000px; overflow: hidden; }
  body {
    background: var(--page);
    font-family: "Lato", Arial, sans-serif;
    display: flex;
    flex-direction: column;
    align-items: center;
    justify-content: center;
    gap: 40px;
  }
  .card {
    position: relative;
    width: 860px;
    height: 435px;
    background: var(--card-black);
    border-radius: 16px;
    overflow: hidden;
    box-shadow: 0 6px 18px rgba(0,0,0,0.25);
  }

  /* Front */
  .front-shatter {
    position: absolute;
    inset: 0 0 60px 0;
    background:
      radial-gradient(ellipse at 50% 5%, var(--glass-light) 0%, rgba(120,120,120,0.75) 25%, rgba(40,40,40,0.9) 60%, var(--card-black) 100%);
  }
  .front-mark {
    position: absolute;
    left: 0; right: 0;
    top: 75px;
    text-align: center;
    font-weight: 900;
    font-size: 290px;
    line-height: 1;
    letter-spacing: 4px;
    color: var(--silver);
  }
  .front-tagline {
    position: absolute;
    left: 0; right: 0; bottom: 0;
    height: 60px;
    background: var(--card-black);
    color: var(--white);
    font-weight: 700;
    font-size: 27px;
    text-align: center;
    line-height: 56px;
  }

  /* Back */
  .back-impact {
    position: absolute;
    top: -10px;
    right: 10px;
    width: 290px;
    height: 290px;
    border-radius: 50%;
    background: radial-gradient(circle at 55% 45%, var(--white) 0%, var(--glass-light) 10%, var(--glass-mid) 40%, rgba(30,30,30,0.6) 65%, transparent 72%);
  }
  .back-name {
    position: absolute;
    left: 0; width: 540px;
    top: 108px;
    text-align: center;
    color: var(--white);
    font-weight: 700;
    font-size: 24px;
    letter-spacing: 1px;
  }
  .back-divider {
    position: absolute;
    left: 35px;
    top: 210px;
    width: 790px;
    height: 40px;
  }
  .back-contacts {
    position: absolute;
    left: 50px;
    top: 300px;
    list-style: none;
    display: flex;
    flex-direction: column;
    gap: 14px;
  }
  .contact-row {
    display: flex;
    align-items: center;
    gap: 14px;
    color: var(--white);
    font-size: 22px;
  }
  .contact-icon { width: 30px; height: 30px; flex: none; }
  .back-abn {
    position: absolute;
    right: 48px;
    bottom: 56px;
    color: var(--muted);
    font-size: 18px;
  }
</style>
</head>
<body>

<section class="card card-front" aria-label="Card front">
  <div class="front-shatter" role="img" aria-label="Shattered windscreen glass radiating from an impact point"></div>
  <div class="front-mark">KLT</div>
  <p class="front-tagline">your local automotive &amp; machinery glass specialist</p>
</section>

<section class="card card-back" aria-label="Card back">
  <div class="back-impact" role="img" aria-label="Cracked glass impact spot"></div>
  <h1 class="back-name">MORRIS</h1>
  <svg class="back-divider" viewBox="0 0 790 40" aria-hidden="true">
    <polyline points="0,30 370,30 390,10 410,30 790,30" fill="none" stroke="#ffffff" stroke-width="4"/>
  </svg>
  <ul class="back-contacts">
    <li class="contact-row">
      <svg class="contact-icon" viewBox="0 0 30 30" aria-hidden="true">
        <circle cx="15" cy="15" r="13" fill="none" stroke="#fff" stroke-width="2"/>
        <path d="M10 8c-2 2-1 6 3 10s8 5 10 3l-3-3-2 1c-2-1-4-3-5-5l1-2z" fill="#fff"/>
      </svg>
      <span>0438 62 57 84</span>
    </li>
    <li class="contact-row">
      <svg class="contact-icon" viewBox="0 0 30 30" aria-hidden="true">
        <circle cx="15" cy="15" r="13" fill="none" stroke="#fff" stroke-width="2"/>
        <text x="15" y="20.5" text-anchor="middle" font-family="Lato, sans-serif" font-weight="700" font-size="16" fill="#fff">@</text>
      </svg>
      <span>morris@kltautoglaze.com.au</span>
    </li>
    <li class="contact-row">
      <svg class="contact-icon" viewBox="0 0 30 30" aria-hidden="true">
        <circle cx="15" cy="15" r="13" fill="none" stroke="#fff" stroke-width="2"/>
        <circle cx="15" cy="15" r="8" fill="none" stroke="#fff" stroke-width="1.5"/>
        <ellipse cx="15" cy="15" rx="3.5" ry="8" fill="none" stroke="#fff" stroke-width="1.5"/>
        <line x1="7" y1="15" x2="23" y2="15" stroke="#fff" stroke-width="1.5"/>
      </svg>
      <span>www.kltautoglaze.com.au</span>
    </li>
  </ul>
  <p class="back-abn">Abn: 52807341196</p>
</section>

</body>
</html>
```